engaging mobile application to encourage lifestyle change

We need an App that will help people get from Bloom 4 Joy. A weight loss program based on realistic and healthy lifestyle modifications. By learning portion control, healthy food choices, and with the encouragement to get moving.
We would like the design to be gender neutral but must be fun.
The final design must be easy to use and useful to our clients.

Target Market(s)

Health, Wellbeing, Weightloss

Industry/Entity Type

Weight

Font styles to use
Sans Serif

Requirements
Must have
• Hydration log, Weigh-ins with fat %, Food log, Location of meetings,lectures and weigh-ins, list of restaurants that comply with B4J, Fitness plan, Mall walk maps, daily motivational message.

```html
<!DOCTYPE html>
<html lang="en">
<head>
<meta charset="utf-8">
<title>Nutrient Insights</title>
<link rel="stylesheet" href="https://fonts.googleapis.com/css2?family=Roboto:wght@400;500&display=swap">
<style>
  :root {
    --app-bar: #ff9800;
    --app-bar-text: #ffffff;
    --chart-bg: #f0f0f2;
    --grid: #d2d2d6;
    --axis: #1a1a1a;
    --label: #333333;
    --bar-light: #aae0fb;
    --bar-mid: #5ebaf5;
    --bar-dark: #4393d4;
    --today: #ff9800;
    --panel: #ffffff;
    --fat-day: #cbd7e6;
    --fat-week: #9ab4d3;
    --fat-month: #6689b3;
    --nav: #000000;
    --nav-icon: #ffffff;
  }
  * { margin: 0; padding: 0; box-sizing: border-box; }
  html, body { width: 750px; height: 1200px; overflow: hidden; background: var(--panel); }
  body { font-family: 'Roboto', Arial, sans-serif; color: var(--label); }
  .screen { position: relative; width: 750px; height: 1200px; overflow: hidden; }

  .app-bar {
    position: absolute; left: 0; top: 0; width: 750px; height: 90px;
    background: var(--app-bar); color: var(--app-bar-text);
  }
  .app-bar .back { position: absolute; left: 10px; top: 24px; }
  .app-bar .mark {
    position: absolute; left: 27px; top: 14px; width: 62px; height: 60px;
    border: 4px solid var(--app-bar-text); border-radius: 10px;
  }
  .app-bar .title {
    position: absolute; left: 103px; top: 21px; font-size: 38px; font-weight: 400;
  }
  .app-bar .status { position: absolute; right: 18px; top: 24px; display: flex; align-items: center; gap: 12px; }
  .app-bar .clock { font-size: 24px; font-weight: 500; }

  .chart-area { position: absolute; left: 0; top: 90px; width: 750px; height: 644px; background: var(--chart-bg); }
  .chart-svg { position: absolute; left: 0; top: 0; }
  .axis-label { font-size: 23px; fill: var(--label); }
  .day-label { font-size: 30px; fill: var(--label); }
  .day-num { font-size: 20px; fill: var(--label); }
  .today-label { font-size: 28px; fill: var(--today); }

  .legend { position: absolute; left: 21px; top: 812px; list-style: none; }
  .legend li { display: flex; align-items: center; height: 32px; font-size: 23px; color: var(--label); }
  .legend .swatch { width: 22px; height: 22px; margin-right: 12px; border-radius: 2px; }
  .swatch.day { background: var(--fat-day); }
  .swatch.week { background: var(--fat-week); }
  .swatch.month { background: var(--fat-month); }

  .fat-svg { position: absolute; left: 0; top: 930px; }
  .fat-title { font-size: 24px; fill: var(--label); }
  .fat-value { font-size: 25px; fill: var(--label); }

  .nav-bar { position: absolute; left: 0; top: 1164px; width: 750px; height: 36px; background: var(--nav); }
</style>
</head>
<body>
<main class="screen">
  <header class="app-bar">
    <svg class="back" width="14" height="40" viewBox="0 0 14 40"><path d="M11 6 L4 20 L11 34" fill="none" stroke="#ffe0b0" stroke-width="3"/></svg>
    <span class="mark"></span>
    <h1 class="title">Nutrient Insights</h1>
    <div class="status">
      <svg width="26" height="24" viewBox="0 0 26 24"><path d="M0 24 L26 0 L26 24 Z" fill="#ffffff"/></svg>
      <svg width="16" height="26" viewBox="0 0 16 26"><rect x="5" y="0" width="6" height="3" fill="#fff"/><rect x="0" y="3" width="16" height="23" rx="1" fill="#fff"/></svg>
      <span class="clock">4:37</span>
    </div>
  </header>

  <section class="chart-area" aria-label="Daily calories chart">
    <svg class="chart-svg" width="750" height="644" viewBox="0 90 750 644">
      <g stroke="var(--grid)" stroke-width="2">
        <line x1="0" y1="197" x2="629" y2="197"/><line x1="0" y1="242" x2="629" y2="242"/>
        <line x1="0" y1="287" x2="629" y2="287"/><line x1="0" y1="331" x2="629" y2="331"/>
        <line x1="0" y1="376" x2="629" y2="376"/><line x1="0" y1="421" x2="629" y2="421"/>
        <line x1="0" y1="466" x2="629" y2="466"/><line x1="0" y1="510" x2="629" y2="510"/>
        <line x1="0" y1="555" x2="629" y2="555"/><line x1="0" y1="600" x2="629" y2="600"/>
        <line x1="0" y1="645" x2="629" y2="645"/><line x1="0" y1="689" x2="629" y2="689"/>
        <line x1="224" y1="177" x2="224" y2="734"/>
      </g>
      <g class="axis-label" text-anchor="start">
        <text x="637" y="205">2,400</text><text x="637" y="250">2,200</text>
        <text x="637" y="295">2,000</text><text x="637" y="339">1,800</text>
        <text x="637" y="384">1,600</text><text x="637" y="429">1,400</text>
        <text x="637" y="474">1,200</text><text x="637" y="518">1,000</text>
        <text x="637" y="563">800</text><text x="637" y="608">600</text>
        <text x="637" y="653">400</text><text x="637" y="697">200</text>
      </g>
      <!-- Saturday -->
      <rect x="0" y="289" width="85" height="90" fill="var(--bar-light)"/>
      <rect x="0" y="379" width="85" height="219" fill="var(--bar-mid)"/>
      <rect x="0" y="598" width="85" height="136" fill="var(--bar-dark)"/>
      <!-- Sunday -->
      <rect x="88" y="334" width="105" height="65" fill="var(--bar-light)"/>
      <rect x="88" y="399" width="105" height="145" fill="var(--bar-mid)"/>
      <rect x="88" y="544" width="105" height="190" fill="var(--bar-dark)"/>
      <!-- Monday -->
      <rect x="255" y="381" width="104" height="104" fill="var(--bar-light)"/>
      <rect x="255" y="485" width="104" height="160" fill="var(--bar-mid)"/>
      <rect x="255" y="645" width="104" height="89" fill="var(--bar-dark)"/>
      <!-- Tuesday -->
      <rect x="362" y="416" width="104" height="77" fill="var(--bar-light)"/>
      <rect x="362" y="493" width="104" height="161" fill="var(--bar-mid)"/>
      <rect x="362" y="654" width="104" height="80" fill="var(--bar-dark)"/>
      <!-- Wednesday -->
      <rect x="471" y="560" width="104" height="49" fill="var(--bar-light)"/>
      <rect x="471" y="609" width="104" height="74" fill="var(--bar-mid)"/>
      <rect x="471" y="683" width="104" height="51" fill="var(--bar-dark)"/>
      <!-- Baseline with today marker -->
      <path d="M0 734 L473 734 L523 686 L573 734 L629 734" fill="none" stroke="var(--axis)" stroke-width="2"/>
      <path d="M475 735 L523 688 L571 735 Z" fill="var(--panel)"/>
      <path d="M473 734 L523 686 L573 734" fill="none" stroke="var(--axis)" stroke-width="2"/>
      <text class="day-label" x="0" y="728">Sa</text><text class="day-num" x="42" y="716">27</text>
      <text class="day-label" x="105" y="728">Su</text><text class="day-num" x="150" y="716">28</text>
      <text class="day-label" x="276" y="728">M</text><text class="day-num" x="313" y="716">29</text>
      <text class="day-label" x="380" y="728">Tu</text><text class="day-num" x="424" y="716">30</text>
      <text class="today-label" x="523" y="727" text-anchor="middle">W</text>
    </svg>
  </section>

  <ul class="legend">
    <li><span class="swatch day"></span>Wed Dec 31 2014</li>
    <li><span class="swatch week"></span>Average for last 7 days</li>
    <li><span class="swatch month"></span>Average for last 28 days</li>
  </ul>

  <svg class="fat-svg" width="750" height="234" viewBox="0 930 750 234" aria-label="Fat calories comparison">
    <g stroke="var(--grid)" stroke-width="2">
      <line x1="222" y1="934" x2="222" y2="1164"/>
      <line x1="411" y1="934" x2="411" y2="1164"/>
      <line x1="601" y1="934" x2="601" y2="1164"/>
    </g>
    <line x1="31" y1="934" x2="31" y2="1164" stroke="#bbbbbb" stroke-width="2"/>
    <text class="fat-title" x="40" y="958">Fat</text>
    <rect x="31" y="967" width="219" height="53" fill="var(--fat-day)"/>
    <text class="fat-value" x="283" y="1003">232 cals</text>
    <rect x="31" y="1028" width="456" height="54" fill="var(--fat-week)"/>
    <text class="fat-value" x="520" y="1064">480 cals</text>
    <rect x="31" y="1088" width="241" height="54" fill="var(--fat-month)"/>
    <text class="fat-value" x="336" y="1124">287 cals</text>
  </svg>

  <nav class="nav-bar" aria-label="System navigation">
    <svg width="750" height="36" viewBox="0 0 750 36">
      <path d="M154 6 L132 18 L154 30 Z" fill="none" stroke="var(--nav-icon)" stroke-width="2"/>
      <circle cx="375" cy="18" r="12" fill="none" stroke="var(--nav-icon)" stroke-width="2"/>
      <rect x="593" y="7" width="23" height="23" fill="none" stroke="var(--nav-icon)" stroke-width="2"/>
    </svg>
  </nav>
</main>
</body>
</html>
```